Bluegull Harbor Tours and Charters

I'm looking to update my current website that was written in Joomla. I would like to move to a more modern design that works well on all platforms using a Wordpress theme. The website is, https://www.bluegullharbortours.example/ It should be noted that I currently have an online booking API (Tidebook) that is integrated with the site but I don't want to worry about that for now. Once I get the new site up and running I am going to move to Quayly which doesn't hook into the site, it just links to an external booking company. Just ignore the Tidebook booking (Book Now) code and build the site. IMPORTANT: My website is hosted on HostMarlow and I currently manage it through cPanel. I want to be able to make changes, updates and manage the website once its completed.

Target Market(s)

Tourists visiting Siesta Key and Venice Florida for Dolphin, sunset tours and private half and full day charters to Pelican Rib Island.

Industry/Entity Type

Tourism

Coding

Coded - Design and coding required

Font styles to use
Other font styles liked:
• Freebooter

Colors
0455a3
85acd3
fbed22
fbee3e
ffc214
ffcf3e
f78f20
faa54b

Requirements
Must have
• Our brand is fun on the water. Social Media links. Great photos, we will provide, and compelling descriptions of each of the tours we offer.
• Dolphin Tours
• Sunset Tours
• Shelling and Snorkeling
• Boating Instruction - I would like this page to have a more professional look and feel. It needs to stand out from the other pages as a professional service yet it still needs to blend well with the entire site.
• What can you do to make this site, https://www.bluegullharbortours.example/ better?
• I don't really need a "Gallery Page" but I want to highlight lots of great pics from our tours. Here is a good example..... check this site out.
• https://brindlecharters.example/
• I don't want to be "like" Brindle Charters, I want my site to be better. This is my competitor.
Nice to have
• I selected some colors for the theme but basically I just want it to be a bright, fun and outgoing site.
• There is a font you can download called Freebooter. It gives it that Pirate look and feel. I would like to use that in some places. Its in my logo on the website. Don't go overboard with the Pirate look and feel but some subtitle pirate things in the site would make it fun.

```html
<!DOCTYPE html>
<html lang="en">
<head>
<meta charset="utf-8">
<title>Bluegull Harbor Tours and Charters</title>
<link rel="stylesheet" href="https://fonts.googleapis.com/css2?family=Raleway:wght@400;500;600;700&family=IM+Fell+English&family=Dancing+Script:wght@500&display=swap">
<style>
:root{
  --blue:#0455a3;
  --blue-light:#85acd3;
  --blue-deep:#0a2a4c;
  --yellow:#fbed22;
  --orange:#f78f20;
  --orange-soft:#faa54b;
  --ink:#1b1b1b;
  --muted:#555;
  --paper:#ffffff;
  --mist:#f1f0ec;
  --footer:#2f3a40;
}
*{box-sizing:border-box;margin:0;padding:0}
html,body{width:1200px;height:3442px;overflow:hidden}
body{position:relative;font-family:"Raleway",sans-serif;color:var(--ink);background:var(--paper)}
.abs{position:absolute}
.btn{position:absolute;display:flex;align-items:center;justify-content:center;background:var(--blue);color:#fff;font-size:12px;border-radius:22px;box-shadow:0 0 0 2px #fff,0 0 0 3px var(--blue-light);text-decoration:none}
.center{text-align:center}

/* hero */
.hero{position:absolute;left:0;top:0;width:1200px;height:734px;background:linear-gradient(160deg,#3b78b8 0%,#1f62a8 40%,#14558f 100%)}
.hero-photo{position:absolute;inset:0;background:radial-gradient(ellipse at 20% 60%,rgba(255,255,255,.18),transparent 55%),linear-gradient(180deg,rgba(10,60,120,.0),rgba(8,50,100,.35))}
.follow{left:218px;top:88px;color:#fff;font-size:11px;display:flex;align-items:center;gap:14px}
.social-dot{width:13px;height:13px;border-radius:50%;background:#fff;opacity:.9}
.brand{left:500px;top:48px;width:200px;color:var(--orange);font-weight:700;font-size:30px;letter-spacing:1px;text-align:center}
.brand small{display:block;font-size:8px;letter-spacing:1px;color:#fff;font-weight:500;margin-top:2px}
.call{left:822px;top:72px;color:#fff;font-size:12px;display:flex;gap:12px;align-items:center}
.call b{display:block;font-weight:600;font-size:12px}
.call span{font-size:10px}
.nav{left:142px;top:167px;width:916px;height:60px;background:#f4f4f4;display:flex;justify-content:center;align-items:center;gap:40px;font-size:11px;font-family:"IM Fell English",serif;color:#222;box-shadow:0 2px 6px rgba(0,0,0,.15)}
.kicker{left:0;width:1200px;top:335px;font-family:"Dancing Script",cursive;color:#fff;font-size:22px}
.kicker-line{left:565px;top:372px;width:70px;height:1px;background:#fff}
.hero-title{left:0;width:1200px;top:385px;color:#fff;font-weight:600;font-size:40px}
.hero-text{left:270px;width:660px;top:462px;color:#fff;font-size:11px;line-height:22px}
.arrow-circle{width:38px;height:38px;border-radius:50%;background:#fff;display:flex;align-items:center;justify-content:center}

/* tours */
.section-title{left:0;width:1200px;font-weight:600;font-size:30px}
.section-text{left:360px;width:480px;font-size:11px;line-height:22px;color:#333}
.tour-card{position:absolute;top:922px;height:372px;padding:18px 14px}
.tour-card .photo{height:154px}
.tour-card h3{margin-top:37px;text-align:center;font-size:17px;font-weight:700}
.tour-card p{margin:14px auto 0;width:200px;text-align:center;font-size:10px;line-height:20px;color:#333}
.yellow{background:var(--yellow)}
.orange{background:var(--orange)}
.pager{width:40px;height:40px;border-radius:50%;background:#eee;display:flex;align-items:center;justify-content:center}

/* ocean feature */
.ocean{position:absolute;left:0;top:1440px;width:1200px;height:544px;background:linear-gradient(180deg,#2c4f74 0%,#11304f 45%,#0b2238 100%)}
.feature-title{left:156px;top:1565px;width:380px;color:#fff;font-family:"IM Fell English",serif;font-size:29px;line-height:50px}
.feature-text{left:156px;top:1706px;width:360px;color:#fff;font-size:11px;line-height:23px}
.video{left:532px;top:1574px;width:528px;height:330px;border:2px solid rgba(255,255,255,.8);background:linear-gradient(180deg,#7fa5c4 0%,#3d6a8e 55%,#2a4e6e 100%)}

/* testimonials */
.testi{position:absolute;left:0;top:1984px;width:1200px;height:549px;background:var(--mist)}
.testi-photo{position:absolute;left:0;top:0;width:760px;height:549px;background:linear-gradient(90deg,#b9b5ab 0%,#d4d1c9 45%,rgba(241,240,236,0) 100%)}
.testi-title{left:756px;top:2040px;width:180px;font-family:"IM Fell English",serif;font-size:28px}
.testi-line{left:800px;top:2097px;width:92px;height:2px;background:var(--blue)}
.quote-card{left:654px;top:2140px;width:406px;height:287px;background:#f7f7f7;border-radius:16px;box-shadow:0 6px 16px rgba(0,0,0,.18)}
.quote-mark{left:654px;width:406px;top:2180px;font-family:"IM Fell English",serif;font-size:80px;line-height:80px}
.quote-text{left:680px;width:354px;top:2268px;font-size:11px;line-height:22px;color:#333}
.quote-name{left:654px;width:406px;top:2370px;font-size:12px;font-weight:700}
.small-pager{width:26px;height:26px;border-radius:50%;background:#fff;display:flex;align-items:center;justify-content:center;box-shadow:0 1px 3px rgba(0,0,0,.15)}

/* offers */
.offer-frame{position:absolute;top:2597px;height:275px;background:#efefef;padding:18px}
.offer-frame .photo{height:239px}
.offer-title{font-family:"IM Fell English",serif;font-size:20px;top:2912px}
.offer-text{font-size:11px;top:2956px}

/* footer */
.footer{position:absolute;left:0;top:3111px;width:1200px;height:293px;background:linear-gradient(180deg,#3a454b,#2a3438)}
.foot-brand{left:168px;top:3226px;width:230px;text-align:center;color:var(--orange);font-weight:700;font-size:30px;letter-spacing:1px}
.foot-brand small{display:block;color:#fff;font-size:8px;font-weight:500;letter-spacing:1px;margin-top:2px}
.foot-fb{left:175px;top:3321px;width:24px;height:24px;border-radius:50%;background:var(--blue)}
.foot-head{font-family:"IM Fell English",serif;color:#fff;font-size:17px;top:3172px}
.foot-rule{top:3200px;width:48px;height:1px;background:#fff}
.foot-link{color:#fff;font-size:10px}
.copyright{left:0;top:3404px;width:1200px;height:38px;background:var(--blue);color:#fff;font-size:11px;display:flex;align-items:center;justify-content:center}
</style>
</head>
<body>

<!-- Hero -->
<header class="hero">
  <div class="hero-photo" role="img" aria-label="Tour boat cruising on blue water with a blue colour wash"></div>
</header>
<div class="abs follow">Follow Us On: <span class="social-dot" role="img" aria-label="Social link"></span><span class="social-dot" role="img" aria-label="Social link"></span><span class="social-dot" role="img" aria-label="Social link"></span></div>
<div class="abs brand">BLUEGULL<small>HARBOR TOURS AND CHARTERS</small></div>
<div class="abs call">
  <svg width="22" height="22" viewBox="0 0 24 24"><circle cx="12" cy="12" r="12" fill="#fff"/><path d="M8.5 6.5l2 2-1.2 1.5c.8 1.7 2 2.9 3.7 3.7l1.5-1.2 2 2-1.3 1.8C11 16 8 13 6.7 7.8z" fill="#0455a3"/></svg>
  <div><b>Call Now!</b><span>555.014.2288</span></div>
</div>
<nav class="abs nav"><span>Home</span><span>Dolphin Tours</span><span>Sunset Tours</span><span>Shelling and Snorkeling</span><span>Boating Instruction</span><span>Contact Us</span></nav>
<div class="abs kicker center">Prepare For</div>
<div class="abs kicker-line"></div>
<h1 class="abs hero-title center">Siesta Key and Venice's #1 Dolphin Tour</h1>
<p class="abs hero-text center">Lorem ipsum dolor sit amet, consectetur adipiscing elit, sed do eiusmod tempor incididunt ut labore et dolore magna aliqua. Ut enim ad minim veniam, quis nostrud exercitation.</p>
<a class="btn" style="left:535px;top:535px;width:133px;height:41px">Let Go!</a>
<div class="abs arrow-circle" style="left:75px;top:403px"><svg width="10" height="12"><path d="M8 1L2 6l6 5" stroke="#333" stroke-width="2" fill="none"/></svg></div>
<div class="abs arrow-circle" style="left:1087px;top:403px"><svg width="10" height="12"><path d="M2 1l6 5-6 5" stroke="#333" stroke-width="2" fill="none"/></svg></div>

<!-- Tours -->
<h2 class="abs section-title center" style="top:786px">Bluegull Harbor Tours and Charters</h2>
<p class="abs section-text center" style="top:843px">Lorem ipsum dolor sit amet, consectetur adipiscing elit, sed do eiusmod tempor incididunt ut labore et dolore magna aliqua.</p>

<article class="tour-card yellow" style="left:142px;width:289px">
  <div class="photo" role="img" aria-label="Dolphin surfacing in green water" style="background:linear-gradient(180deg,#6fb3a4,#3f8577)"></div>
  <h3>Dolphine Tours</h3>
  <p>Lorem ipsum dolor sit amet, consectetur adipiscing elit.</p>
</article>
<article class="tour-card orange" style="left:454px;width:292px">
  <div class="photo" role="img" aria-label="Sailboat at sunset under orange clouds" style="background:linear-gradient(180deg,#3a4a66 0%,#e08a3c 60%,#2b2420 100%)"></div>
  <h3>Sunset Tours</h3>
  <p>Lorem ipsum dolor sit amet, consectetur adipiscing elit.</p>
</article>
<article class="tour-card yellow" style="left:768px;width:290px">
  <div class="photo" role="img" aria-label="Seashell lying on white sand" style="background:linear-gradient(180deg,#d9d8d4,#bdbab3)"></div>
  <h3>Shelling and Snorkeling</h3>
  <p>Lorem ipsum dolor sit amet, consectetur adipiscing elit.</p>
</article>
<a class="btn" style="left:222px;top:1232px;width:130px;height:41px">Let Go!</a>
<a class="btn" style="left:536px;top:1232px;width:130px;height:41px">Let Go!</a>
<a class="btn" style="left:849px;top:1232px;width:130px;height:41px">Let Go!</a>
<div class="abs pager" style="left:551px;top:1340px"><svg width="8" height="10"><path d="M6 1L2 5l4 4" stroke="#999" stroke-width="1.5" fill="none"/></svg></div>
<div class="abs pager" style="left:606px;top:1340px"><svg width="8" height="10"><path d="M2 1l4 4-4 4" stroke="#999" stroke-width="1.5" fill="none"/></svg></div>

<!-- Ocean feature -->
<section class="ocean" role="img" aria-label="Dolphin fin breaking the surface of dark open water"></section>
<svg class="abs" style="left:0;top:1440px" width="1200" height="60" viewBox="0 0 1200 60"><path d="M0 0H1200V22C1000 40 820 10 600 26S220 44 0 18Z" fill="#fff"/></svg>
<h2 class="abs feature-title">Dolphin Sightseeing and Sunset Tours!</h2>
<p class="abs feature-text">Our goal is for you to have your best vacation day ever as we take you out on the water with Our Adventure. We offer sightseeing tours, dolphin boat rides or special event services. It's your adventure, let us take you there.</p>
<a class="btn" style="left:156px;top:1835px;width:131px;height:39px">Read More</a>
<div class="abs video" role="img" aria-label="Video still of guests smiling aboard a boat"></div>
<svg class="abs" style="left:762px;top:1705px" width="70" height="70" viewBox="0 0 70 70"><circle cx="35" cy="35" r="31" fill="none" stroke="#fff" stroke-width="5"/><path d="M28 22l20 13-20 13z" fill="#fff"/></svg>

<!-- Testimonials -->
<section class="testi"><div class="testi-photo" role="img" aria-label="Woman in a captain's hat looking through binoculars from a boat"></div></section>
<h2 class="abs testi-title center">Testimonials</h2>
<div class="abs testi-line"></div>
<div class="abs quote-card"></div>
<div class="abs quote-mark center">&ldquo;</div>
<p class="abs quote-text center">Lorem ipsum dolor sit amet, consectetur adipiscing elit, sed do eiusmod tempor incididunt ut labore et dolore magna aliqua. Ut enim ad minim veniam, quis nostrud</p>
<div class="abs quote-name center">Name Here</div>
<div class="abs small-pager" style="left:822px;top:2451px"><svg width="6" height="8"><path d="M5 1L1 4l4 3" stroke="#666" fill="none"/></svg></div>
<div class="abs small-pager" style="left:863px;top:2451px"><svg width="6" height="8"><path d="M1 1l4 3-4 3" stroke="#666" fill="none"/></svg></div>

<!-- Offers -->
<div class="offer-frame" style="left:142px;width:445px"><div class="photo" role="img" aria-label="Charter boat on green water with a dolphin alongside" style="background:linear-gradient(180deg,#8fb7d4 0%,#4fa89a 45%,#2f8478 100%)"></div></div>
<div class="offer-frame" style="left:612px;width:446px"><div class="photo" role="img" aria-label="White gift box tied with a red ribbon bow" style="background:#fbfaf6"></div></div>
<h3 class="abs offer-title center" style="left:142px;width:445px">Custom Destination Charter</h3>
<p class="abs offer-text center" style="left:142px;width:445px">We'll get you to that perfect spot for the day!</p>
<h3 class="abs offer-title center" style="left:612px;width:446px">Gift Card</h3>
<p class="abs offer-text center" style="left:612px;width:446px">Lorem ipsum dolor sit amet, consectetur adipiscing elit</p>
<a class="btn" style="left:300px;top:3010px;width:131px;height:39px">Book Now</a>
<a class="btn" style="left:771px;top:3010px;width:128px;height:39px">Buy Card</a>

<!-- Footer -->
<footer class="footer" role="img" aria-label="Faint underwater backdrop"></footer>
<div class="abs foot-brand">BLUEGULL<small>HARBOR TOURS AND CHARTERS</small></div>
<div class="abs foot-fb" role="img" aria-label="Social link"></div>

<div class="abs foot-head" style="left:525px">Quick Links</div>
<div class="abs foot-rule" style="left:525px"></div>
<div class="abs foot-link" style="left:525px;top:3226px">&rsaquo;&nbsp; Home</div>
<div class="abs foot-link" style="left:525px;top:3265px">&rsaquo;&nbsp; Dolphine Tours</div>
<div class="abs foot-link" style="left:525px;top:3304px">&rsaquo;&nbsp; Sunset Tours</div>
<div class="abs foot-link" style="left:672px;top:3226px">&rsaquo;&nbsp; Shelling and Snorkeling</div>
<div class="abs foot-link" style="left:672px;top:3265px">&rsaquo;&nbsp; Boating Instruction</div>
<div class="abs foot-link" style="left:672px;top:3304px">&rsaquo;&nbsp; Contact Us</div>

<div class="abs foot-head" style="left:849px">Contact Us</div>
<div class="abs foot-rule" style="left:849px"></div>
<div class="abs foot-link" style="left:857px;top:3226px;display:flex;gap:10px;align-items:center"><svg width="10" height="10" viewBox="0 0 24 24"><path d="M6 2l4 4-2 3c1.5 3 4 5.5 7 7l3-2 4 4-3 4C10 21 3 14 2 5z" fill="#fff"/></svg>555.014.2288</div>
<div class="abs foot-link" style="left:857px;top:3271px;display:flex;gap:10px;align-items:center"><svg width="10" height="8" viewBox="0 0 20 16"><rect width="20" height="16" fill="#fff"/><path d="M0 0l10 8 10-8" stroke="#2f3a40" stroke-width="2" fill="none"/></svg>hello@bluegullharbor.example</div>
<div class="abs foot-link" style="left:857px;top:3300px;display:flex;gap:10px;align-items:center"><svg width="9" height="12" viewBox="0 0 18 24"><path d="M9 0a9 9 0 0 1 9 9c0 7-9 15-9 15S0 16 0 9a9 9 0 0 1 9-9z" fill="#fff"/><circle cx="9" cy="9" r="3" fill="#2f3a40"/></svg>123 Lorem Ipsum,City name</div>

<div class="abs copyright">Copyright &copy; 2019 Bluegull</div>
</body>
</html>
```